Tova Brisk Fitness Coaching Project

I am a personal trainer based in London. My services include one-on-one PT sessions, bootcamps.
I would like the design to be minimalistic. With light colours: white, pink, purple.
I specialise in weight loss, flexibility, mobility.

Tova Penrick
Personal Trainer
Email: tova.penrick@mailgrove.net
tel: 07500 918 243
Instagram: Tova Brisk

Target Market(s)

adults, mostly females (age 18-50).

Industry/Entity Type

Fitness

Contact Information for Business Card

Tova Penrick
Personal Trainer
tel: 07500 918 243
Instagram: Tova Brisk

Font styles to use
Serif

Colors
eea4c8
fbd4d5
fdf9cf
cfeae6
cee9f5

Requirements
Nice to have
• minimalistic style
• easy to read and remember

```html
<!DOCTYPE html>
<html lang="en">
<head>
<meta charset="utf-8">
<title>Tova Penrick – Personal Trainer Business Card</title>
<link rel="stylesheet" href="https://fonts.googleapis.com/css2?family=Open+Sans:wght@400;700&display=swap">
<style>
  :root {
    --pink: #eea4c8;
    --pink-bright: #fcb0d6;
    --blush: #fbd4d5;
    --cream: #fdf9cf;
    --ink: #6e6e6e;
    --ink-soft: #8a8a8a;
    --paper: #ffffff;
    --backdrop: #e4e4e6;
  }
  * { box-sizing: border-box; margin: 0; padding: 0; }
  html, body { width: 1200px; height: 876px; overflow: hidden; }
  body {
    background: var(--backdrop);
    font-family: "Open Sans", Arial, sans-serif;
    position: relative;
  }
  .card {
    position: absolute;
    top: 158px;
    width: 360px;
    height: 560px;
    background: var(--paper);
    overflow: hidden;
    box-shadow: 0 6px 18px rgba(0,0,0,0.12);
  }
  .card--front { left: 180px; }
  .card--back { left: 660px; }

  .band { position: absolute; left: 0; width: 100%; height: 36px; }
  .card--front .band { background: var(--pink); }
  .card--back .band { background: var(--blush); }
  .band--top { top: 0; }
  .band--bottom { bottom: 0; }

  .athlete-figure {
    position: absolute;
    left: 40px;
    top: 70px;
    width: 230px;
    height: 440px;
    background: linear-gradient(180deg, var(--blush), #f8c9cb);
    border-radius: 40px 40px 10px 10px;
  }

  .edge-tab { position: absolute; width: 26px; height: 60px; }
  .edge-tab--left { left: 0; top: 112px; }
  .edge-tab--right { right: 0; top: 270px; }

  .identity { position: absolute; left: 58px; top: 150px; }
  .identity__name {
    font-weight: 700;
    font-size: 34px;
    color: var(--ink);
    letter-spacing: 0.5px;
    line-height: 1;
  }
  .identity__role {
    margin-top: 6px;
    font-size: 17px;
    color: var(--ink-soft);
    letter-spacing: 4px;
  }

  .contact-list {
    position: absolute;
    left: 0;
    top: 330px;
    width: 330px;
    list-style: none;
  }
  .contact-list__item {
    height: 64px;
    display: flex;
    align-items: center;
    padding-left: 34px;
    gap: 22px;
    background: var(--pink);
    color: var(--cream);
    font-size: 16px;
  }
  .contact-list__item:nth-child(2) { background: var(--pink-bright); }
  .contact-list__icon {
    width: 36px;
    height: 36px;
    flex: none;
    background: var(--cream);
    border-radius: 3px;
    display: flex;
    align-items: center;
    justify-content: center;
  }
  .contact-list__icon svg { width: 22px; height: 22px; }
</style>
</head>
<body>
  <section class="card card--front">
    <div class="band band--top"></div>
    <div class="athlete-figure" role="img" aria-label="Soft pink silhouette of a woman in a standing split stretch"></div>
    <div class="band band--bottom"></div>
  </section>

  <section class="card card--back">
    <div class="band band--top"></div>
    <svg class="edge-tab edge-tab--left" viewBox="0 0 26 60" aria-hidden="true"><polygon points="0,0 26,30 0,60" fill="var(--pink)"/></svg>
    <svg class="edge-tab edge-tab--right" viewBox="0 0 26 60" aria-hidden="true"><polygon points="26,0 0,30 26,60" fill="var(--pink)"/></svg>

    <div class="identity">
      <h1 class="identity__name">Tova Penrick</h1>
      <p class="identity__role">Personal Trainer</p>
    </div>

    <ul class="contact-list">
      <li class="contact-list__item">
        <span class="contact-list__icon">
          <svg viewBox="0 0 24 24" aria-hidden="true"><path d="M6.6 10.8a15 15 0 0 0 6.6 6.6l2.2-2.2a1 1 0 0 1 1-.25 11.4 11.4 0 0 0 3.6.57 1 1 0 0 1 1 1V20a1 1 0 0 1-1 1A17 17 0 0 1 3 4a1 1 0 0 1 1-1h3.5a1 1 0 0 1 1 1c0 1.25.2 2.45.57 3.57a1 1 0 0 1-.25 1z" fill="var(--pink)"/></svg>
        </span>
        <span>07500 918 243</span>
      </li>
      <li class="contact-list__item">
        <span class="contact-list__icon">
          <svg viewBox="0 0 24 24" aria-hidden="true"><rect x="5" y="5" width="14" height="14" fill="var(--pink)"/></svg>
        </span>
        <span>Tova Brisk</span>
      </li>
      <li class="contact-list__item">
        <span class="contact-list__icon">
          <svg viewBox="0 0 24 24" aria-hidden="true"><rect x="3" y="6" width="18" height="12" fill="none" stroke="var(--pink)" stroke-width="1.8"/><polyline points="3,6 12,13 21,6" fill="none" stroke="var(--pink)" stroke-width="1.8"/></svg>
        </span>
        <span>tova.penrick@mailgrove.net</span>
      </li>
    </ul>

    <div class="band band--bottom"></div>
  </section>
</body>
</html>
```